Velmora Fresh Greens Square Trifold Brochure

We need a powerful informational square tri-fold brochure for a new product that is set to change the health of us all. Known as Spirulina, a blue green algae superfood, consumed by people for thousands of years. The reason why life exists on this planet. Sold commercially in stores worldwide as a supplement in dead powder form, until now! We have perfected systems to capture the delicate cells, pack and ship to customers fresh. This whole food gourmet supreme is a game changer for us all.
We need an educational informational card that dramatically captures the attention of everyone. Giving them enough information to bring their curiosity and intrigue to the website to learn more but also having good knowledge base to hold in their hand for those that don't use a computer.
The front of the card should grab their attention (possibly with image of the jar with water below) with the rest for more detailed information, making it clear that this is delicious, raw, living, fresh, pure, super nutrition grown in USA, safe, laboratory tested, etc.
Design should match font, color and design of the website. Very clear, professional, eye catching and very powerful and dramatic. Looking for the best ever!
The ultimate living enzymatically active bioavailable raw plant based nutrients. Grown in spring water using the highest quality natural and organic food grade nutrients, in enclosed greenhouses in Florida.
When we say fresh, we really mean it!
The only truly living Spirulina.
You have to try it at least once.

**May add a bit of sex appeal if done with class. www.velmorafreshgreens.example

Thank you so much, extra special reward for the designer who grabs our attention the best!
Please contact us if you need additional images from the website for your design. Design Ideas we like that grabbed our attention attached below. Just ideas.

Target Market(s)

Health conscious, vegan, bodybuilding, sexy, fitness,

Industry/Entity Type

Health And Wellness

Font styles to use
Serif
Sans Serif

Colors

Designer to choose colors to be used in the design.

Requirements
Must have
• Square design, Powerful info - graphic(s), Color theme to match website and brand. Dynamic message knowledge based theme. Love simple design easy to read. Sections:
• Front cover: Product Jar with water (image) dramatic
• (Sections from Website) Health Benefits, Nutritional Profile, Lab Tested, How its Grown, What is Velmora Fresh Greens,
• Bold Plant based Images to highlight plant based Nutrition
• Include Section with Institutional Quotes KELT, BRMQ, GLX, etc.
Nice to have
• Love to see very creative outside the box design. A Wow head turner! Sexy but simple, classy and elegant.
Should not have
• Please no clutter.

```html
<!DOCTYPE html>
<html lang="en">
<head>
<meta charset="utf-8">
<title>Velmora Fresh Greens – Trifold Brochure</title>
<link href="https://fonts.googleapis.com/css2?family=Montserrat:wght@400;600;700;800&family=Open+Sans:wght@400;600&display=swap" rel="stylesheet">
<style>
  :root{
    --navy:#1d5675;
    --navy-deep:#15445f;
    --teal:#3c9c86;
    --teal-light:#58b39d;
    --leaf:#3a9a43;
    --ink:#2b2b2b;
    --forest:#1e4a2c;
    --paper:#ffffff;
    --mist:#e6e8ea;
    --mist-dark:#d3d6d9;
    --stage:#5f5f5f;
  }
  *{box-sizing:border-box;margin:0;padding:0}
  html,body{width:902px;height:1200px;overflow:hidden;background:var(--stage)}
  .brochure{position:absolute;left:0;top:249px;width:902px;height:702px;background:var(--paper);overflow:hidden;font-family:"Open Sans",Arial,sans-serif;color:var(--ink)}
  .panel{position:absolute;top:0;height:702px}
  .panel--inside{left:0;width:308px;background:var(--paper)}
  .panel--back{left:308px;width:296px}
  .panel--front{left:604px;width:298px;background:var(--teal)}

  /* inside panel */
  .grown-box{position:absolute;left:17px;top:27px;width:291px;height:470px;background:var(--navy);border-top-left-radius:40px}
  .grown-title{position:absolute;left:28px;top:22px;font-family:"Montserrat",sans-serif;color:#fff;font-size:19px;line-height:23px;letter-spacing:1px;padding-right:10px;border-right:3px solid #fff}
  .grown-title b{font-weight:700;display:block}
  .grown-title span{font-weight:400;display:block}
  .section-tag{position:absolute;left:0;height:22px;width:112px;background:var(--teal-light);color:#fff;font-family:"Montserrat",sans-serif;font-weight:700;font-size:11px;line-height:22px;padding-left:22px}
  .section-photo{position:absolute;left:112px;width:166px;border:2px solid #fff}
  .section-copy{position:absolute;left:23px;width:258px;color:#fff;font-size:7.6px;line-height:9.6px;text-align:justify}
  .qualities{position:absolute;left:0;top:485px;width:308px;height:217px;background:var(--paper);border-top-right-radius:36px}
  .qualities h3{position:absolute;left:20px;top:12px;font-family:"Montserrat",sans-serif;font-weight:600;font-size:11.5px;color:var(--teal);letter-spacing:.3px}
  .quality{position:absolute;display:flex;gap:6px;width:128px}
  .quality svg{flex:none}
  .quality b{display:block;font-size:6.6px;font-weight:600;color:#333;letter-spacing:.2px}
  .quality p{font-size:6.4px;line-height:8px;color:#555}

  /* back panel */
  .back-wash{position:absolute;inset:0;background:linear-gradient(170deg,var(--mist) 0%,#f1f2f3 45%,var(--mist-dark) 100%)}
  .back-art{position:absolute;left:50px;top:330px;width:200px;height:190px;border-radius:50%;background:radial-gradient(circle at 45% 45%,#fbfbfb 0%,#ececec 55%,rgba(230,232,234,0) 72%)}
  .brand{position:absolute;text-align:center;font-family:"Montserrat",sans-serif;font-weight:800;color:var(--ink);line-height:1}
  .brand .dot{display:block;margin:0 auto 6px;width:14px;height:14px;border-radius:50%;background:var(--teal)}
  .brand--back{left:0;width:296px;top:430px;font-size:25px}
  .contacts{position:absolute;left:25px;top:562px;list-style:none;font-size:13px;color:var(--ink)}
  .contacts li{display:flex;align-items:center;gap:6px;height:22px}

  /* front panel */
  .cell-photo{position:absolute;left:0;top:0;width:86px;height:702px;background:linear-gradient(180deg,#1f5a6e 0%,#2c6d6a 30%,var(--teal) 55%,#2a6a6a 80%,#1c4f5e 100%)}
  .front-head{position:absolute;left:49px;top:0;width:249px;height:153px;background:var(--paper);border-bottom-left-radius:44px}
  .brand--front{left:0;width:249px;top:44px;font-size:25px}
  .hero-card{position:absolute;left:-21px;top:200px;width:286px;height:440px;background:var(--paper);border-top-left-radius:40px}
  .jar-photo{position:absolute;left:14px;top:6px;width:258px;height:296px;border-radius:20px;background:radial-gradient(ellipse at 50% 40%,#3f7d3a 0%,#2f6b35 30%,#9cd3e6 55%,#e6f4f9 75%,#ffffff 100%)}
  .hero-card h2{position:absolute;left:0;width:286px;top:316px;text-align:center;font-family:"Montserrat",sans-serif;font-weight:600;font-size:18px;line-height:26px;color:var(--forest);letter-spacing:.3px}
  .hero-bar{position:absolute;left:42px;top:374px;width:210px;height:16px;background:var(--leaf);color:#fff;font-family:"Montserrat",sans-serif;font-weight:600;font-size:9px;line-height:16px;text-align:center}
  .hero-note{position:absolute;left:0;width:286px;top:398px;text-align:center;font-family:"Montserrat",sans-serif;font-weight:600;font-size:9px;color:var(--ink)}
  .front-url{position:absolute;right:12px;top:667px;color:#fff;font-family:"Montserrat",sans-serif;font-weight:600;font-size:11px}
</style>
</head>
<body>
<main class="brochure">

  <section class="panel panel--inside">
    <div class="grown-box">
      <h2 class="grown-title"><span>HOW IT'S</span><b>GROWN</b></h2>
    </div>

    <div class="section-tag" style="top:130px">FARMING</div>
    <div class="section-photo" role="img" aria-label="Enclosed greenhouse domes on the farm" style="top:117px;height:51px;background:linear-gradient(180deg,#eef2f5 0%,#c9d2d8 55%,#8e9aa1 100%)"></div>
    <p class="section-copy" style="top:180px">Velmora Fresh Greens is a unique strain of algae grown at a state-of-the-art micro farm in closed-source freshwater raceway systems to keep the growing environment as optimized and clean as possible. Our year-round systems, located in Florida, are regularly cleaned, and live cultures are added to our fresh spring water to maintain a stable growing environment and high nutritional standards for every crop.</p>

    <div class="section-tag" style="top:298px">HARVESTING</div>
    <div class="section-photo" role="img" aria-label="Close-up of fresh green harvest in hand" style="top:278px;height:62px;background:linear-gradient(135deg,#a9c6a5 0%,#6f9a72 50%,#49704d 100%)"></div>
    <p class="section-copy" style="top:346px">Velmora Fresh Greens is a fragile organism (like tiny water balloons) with no cellulose structure to the cell membrane. Because of this the challenge to protect the integrity of these superior nutrients found inside the cell has always been a top priority. If the cells are damaged, the nutrients are dramatically compromised. After many years of research designing and testing experimental systems, we finally solved this problem. Harvesting fresh Velmora Fresh Greens is now the gold standard for protecting the bioavailability of the most powerful nutrition our planet has to offer us.</p>

    <div class="qualities">
      <h3>SUPREME QUALITIES</h3>

      <div class="quality" style="left:20px;top:42px"><svg width="20" height="20" viewBox="0 0 20 20"><circle cx="10" cy="10" r="9" fill="none" stroke="#333" stroke-width="1.3"/><path d="M6 11c2-5 6-5 8-6-1 4-3 8-8 6z" fill="#333"/></svg><div><b>VEGAN</b><p>We use 100% plant and soil based nutrients to grow.</p></div></div>
      <div class="quality" style="left:20px;top:84px"><svg width="20" height="20" viewBox="0 0 20 20"><circle cx="10" cy="10" r="9" fill="none" stroke="#333" stroke-width="1.3"/><path d="M5 15L15 5M7 12c1-4 4-6 7-6-1 3-3 6-7 6z" stroke="#333" stroke-width="1.3" fill="none"/></svg><div><b>GMO FREE</b><p>Single origin as nature intended.</p></div></div>
      <div class="quality" style="left:20px;top:125px"><svg width="20" height="20" viewBox="0 0 20 20"><circle cx="10" cy="10" r="9" fill="none" stroke="#333" stroke-width="1.3"/><path d="M10 4c-3 0-5 2-5 5 0 4 5 7 5 7s5-3 5-7c0-3-2-5-5-5z" fill="var(--teal)"/></svg><div><b>USA GROWN</b><p>Locally produced fresh food is best.</p></div></div>
      <div class="quality" style="left:20px;top:163px"><svg width="20" height="20" viewBox="0 0 20 20"><circle cx="10" cy="10" r="9" fill="none" stroke="#333" stroke-width="1.3"/><path d="M6 14c1-6 5-8 9-8-1 5-4 8-9 8z" fill="#333"/></svg><div><b>RAW</b><p>Truly raw in its pure natural state.</p></div></div>

      <div class="quality" style="left:155px;top:22px"><svg width="20" height="20" viewBox="0 0 20 20"><circle cx="10" cy="10" r="9" fill="none" stroke="#333" stroke-width="1.3"/><path d="M8 5h4M9 5v4l-3 6h8l-3-6V5" stroke="#333" stroke-width="1.2" fill="none"/></svg><div><b>LAB TESTED</b><p>Routine BRMQ/NRVA third party laboratory testing.</p></div></div>
      <div class="quality" style="left:155px;top:60px"><svg width="20" height="20" viewBox="0 0 20 20"><circle cx="10" cy="10" r="9" fill="none" stroke="#333" stroke-width="1.3"/><circle cx="10" cy="10" r="5" fill="var(--leaf)"/></svg><div><b>FRESH</b><p>From our farm to your spoon in 2 days.</p></div></div>
      <div class="quality" style="left:155px;top:105px"><svg width="20" height="20" viewBox="0 0 20 20"><circle cx="10" cy="10" r="9" fill="none" stroke="#333" stroke-width="1.3"/><path d="M10 5v10M5 10h10" stroke="#333" stroke-width="1.4"/></svg><div><b>NATURAL</b><p>Produced by nature not a laboratory.</p></div></div>
      <div class="quality" style="left:155px;top:143px"><svg width="20" height="20" viewBox="0 0 20 20"><circle cx="10" cy="10" r="9" fill="none" stroke="#333" stroke-width="1.3"/><path d="M5 5l10 10" stroke="#333" stroke-width="1.4"/><circle cx="10" cy="10" r="4" fill="none" stroke="#333" stroke-width="1.2"/></svg><div><b>NO FILLERS</b><p>No dangerous additives to worry about here.</p></div></div>
      <div class="quality" style="left:155px;top:182px"><svg width="20" height="20" viewBox="0 0 20 20"><circle cx="10" cy="10" r="9" fill="none" stroke="#333" stroke-width="1.3"/><path d="M6 12a4 4 0 0 0 8 0V7" stroke="#333" stroke-width="1.3" fill="none"/></svg><div><b>DOCTOR RECOMMENDED</b><p>Velmora Fresh Greens is the key to many.</p></div></div>
    </div>
  </section>

  <section class="panel panel--back">
    <div class="back-wash" role="img" aria-label="Soft grey background of floating algae cells and molecule lines"></div>
    <div class="back-art" role="img" aria-label="Spoonful of fresh green paste"></div>
    <div class="brand brand--back"><span class="dot"></span>VELMORA<br>FRESH GREENS</div>
    <ul class="contacts">
      <li><svg width="11" height="11" viewBox="0 0 12 12"><circle cx="6" cy="6" r="5" fill="none" stroke="#333" stroke-width="1.2"/><path d="M1 6h10M6 1c-3 3-3 7 0 10M6 1c3 3 3 7 0 10" stroke="#333" stroke-width=".9" fill="none"/></svg>www.velmorafreshgreens.example</li>
      <li><svg width="11" height="9" viewBox="0 0 12 9"><rect width="12" height="9" fill="#333"/><path d="M0 0l6 5 6-5" stroke="#fff" stroke-width="1" fill="none"/></svg>info@velmorafreshgreens.example</li>
      <li><svg width="14" height="14" viewBox="0 0 14 14"><circle cx="7" cy="7" r="6" fill="none" stroke="#333" stroke-width="1.2"/><path d="M5 4l1 2-1 1c.5 1 1 1.5 2 2l1-1 2 1-1 1.5c-3 0-5-2-5.5-5z" fill="#333"/></svg>555-014-2290</li>
    </ul>
  </section>

  <section class="panel panel--front">
    <div class="cell-photo" role="img" aria-label="Microscope view of blue-green algae cells"></div>
    <div class="front-head">
      <div class="brand brand--front"><span class="dot"></span>VELMORA<br>FRESH GREENS</div>
    </div>
    <div class="hero-card">
      <div class="jar-photo" role="img" aria-label="Jar of fresh green spirulina splashing into clear water"></div>
      <h2>WHEN WE SAY FRESH,<br>WE REALLY MEAN IT!</h2>
      <div class="hero-bar">THE ONLY TRULY LIVING SPIRULINA.</div>
      <p class="hero-note">YOU HAVE TO TRY IT AT LEAST ONCE.</p>
    </div>
    <div class="front-url">www.velmorafreshgreens.example</div>
  </section>

</main>
</body>
</html>
```